School Communication Email Template

Looking for a designer to create a couple simple email templates that are matching our brand colors and feel. Attached is the default email template that is currently being sent out. Company details can be shared upon request.

Template is to be used within the booking tool we use (snapshot below) and gmail. Template code is in HTML (see screenshot below).
Updates

Template code for website should be in HTML. Sorry if that created confusion.

Target Market(s)

Parents of kids enrolled in our classes

Industry/Entity Type

Kids sport classes

Font styles to use
Serif

Colors
0054AA
0677BA
7BADD7
CADEEF
E8F1F8
FFF300
FFF600
FEFA6F
FFFEC7
FFFEE8

Requirements
Must have
• Consistency with company brand/colors
Nice to have
• Flexibility to be adjusted as needed

```html
<!DOCTYPE html>
<html lang="en">
<head>
<meta charset="utf-8">
<title>Booking Confirmation</title>
<link href="https://fonts.googleapis.com/css2?family=Roboto:wght@400;500;700&family=Tinos:wght@700&display=swap" rel="stylesheet">
<style>
:root{
  --page:#e8f1f8;
  --header-grey:#e0e0e0;
  --navy:#243c88;
  --brand:#0054aa;
  --brand-mid:#0677ba;
  --cell:#e8f1f8;
  --cell-border:#a9c6e4;
  --frame:#b9c6d8;
  --gold:#f6b21b;
  --yellow:#fff300;
  --text:#3a3a3a;
  --white:#ffffff;
}
*{box-sizing:border-box;margin:0;padding:0}
html,body{width:713px;height:1200px;overflow:hidden;background:var(--page);font-family:'Roboto',Arial,sans-serif;color:var(--text)}
.email{position:absolute;left:125px;top:26px;width:463px;height:1092px;background:var(--white)}
.masthead{position:absolute;left:0;top:0;width:463px;height:122px;background:var(--header-grey);display:flex;align-items:center;justify-content:center;gap:8px}
.brand-dot{width:14px;height:14px;border-radius:50%;background:var(--gold)}
.brand-name{font-family:'Roboto',Arial,sans-serif;font-weight:700;font-size:18px;color:var(--navy)}
.centered{position:absolute;left:0;width:463px;text-align:center}
.headline{top:142px;font-family:'Tinos','Times New Roman',serif;font-weight:700;font-size:26px;color:var(--navy)}
.subline{top:183px;font-size:11.5px;color:#111}
.divider{position:absolute;left:207px;top:209px;width:49px;height:4px;background:var(--navy)}
.greeting{top:251px;font-size:11.5px;color:#222}
.recipient{top:272px;font-family:'Tinos','Times New Roman',serif;font-weight:700;font-size:16px;color:var(--gold)}
.intro{top:300px;left:90px;width:283px;font-size:11px;line-height:21.5px;color:#444}
.intro strong{font-weight:500;color:#333}
.details{position:absolute;left:40px;top:365px;width:384px;height:348px;border:1.5px solid var(--frame);padding:8px 6px}
.details-title{height:53px;background:var(--brand);color:var(--white);font-family:'Tinos','Times New Roman',serif;font-weight:700;font-size:16px;letter-spacing:2px;display:flex;align-items:center;justify-content:center}
.row{display:flex;justify-content:space-between;height:28.5px;margin-top:5px}
.row:first-of-type{margin-top:9px}
.label{width:160px;background:var(--brand-mid);color:var(--white);font-size:10.5px;display:flex;align-items:center;padding-left:7px}
.value{width:200px;background:var(--cell);border:1.5px solid var(--cell-border);color:#222;font-size:10px;display:flex;align-items:center;padding-left:6px}
.manage-note{top:736px;font-size:11.5px;color:#444}
.manage-btn{position:absolute;left:140px;top:768px;width:185px;height:29px;background:var(--yellow);border:1.5px solid #e6dd3a;color:#333;font-size:9.5px;letter-spacing:.4px;display:flex;align-items:center;justify-content:center}
.appt-id{top:812px;font-size:10.5px;color:#444}
.appt-id strong{font-weight:500}
.signoff{top:862px;font-family:'Tinos','Times New Roman',serif;font-weight:700;font-size:13.5px;color:#111}
.team{top:884px;font-size:11.5px;font-weight:500;color:var(--navy)}
.footer{position:absolute;left:0;top:917px;width:463px;height:175px;background:var(--brand);color:var(--white)}
.footer-brand{position:absolute;top:44px;left:0;width:463px;display:flex;align-items:center;justify-content:center;gap:7px}
.footer-brand .brand-name{color:var(--white);font-size:15px}
.footer-line{position:absolute;left:0;width:463px;text-align:center;font-size:10.3px;line-height:14px;letter-spacing:.3px;color:var(--white)}
.footer-phone{top:102px}
.footer-web{top:119px}
.footer-address{top:139px}
.social{position:absolute;top:1137px;left:305px;display:flex;gap:10px}
.social span{width:26px;height:26px;border-radius:50%;background:var(--navy)}
.social span:last-child{margin-left:6px}
</style>
</head>
<body>
<div class="email">
  <header class="masthead"><span class="brand-dot"></span><span class="brand-name">Bright Star Kids</span></header>
  <h1 class="centered headline">Thank You!</h1>
  <p class="centered subline">Your Booking has been confirmed.</p>
  <div class="divider"></div>
  <p class="centered greeting">Hello</p>
  <p class="centered recipient">Lily Harper</p>
  <p class="centered intro">Your Booking confirmed with <strong>Company Name</strong>. Please find the details below.</p>

  <section class="details">
    <div class="details-title">BOOKING DETAILS</div>
    <div class="row"><div class="label">Student First Name</div><div class="value">Lily</div></div>
    <div class="row"><div class="label">Student Last Name</div><div class="value">Harper</div></div>
    <div class="row"><div class="label">Appointment Name</div><div class="value">Dummy Appointment</div></div>
    <div class="row"><div class="label">Appointment Service</div><div class="value">Dummy Service</div></div>
    <div class="row"><div class="label">Booking Start Date</div><div class="value">21st Feb, 2023</div></div>
    <div class="row"><div class="label">Booking End Date</div><div class="value">23rd Feb, 2023</div></div>
    <div class="row"><div class="label">Appointment Start Time</div><div class="value">Morning 11.00 AM</div></div>
    <div class="row"><div class="label">Appointment&nbsp; End Time</div><div class="value">Afternoon : 4:30 PM</div></div>
  </section>

  <p class="centered manage-note">Manage or edit your appointment online through our portal.</p>
  <div class="manage-btn">MANAGE MY APPOINTMENT</div>
  <p class="centered appt-id"><strong>Appointmnet ID:</strong> ABCD123456</p>
  <p class="centered signoff">Thanks</p>
  <p class="centered team">Team Online Portal</p>

  <footer class="footer">
    <div class="footer-brand"><span class="brand-dot"></span><span class="brand-name">Bright Star Kids</span></div>
    <p class="footer-line footer-phone">(555) 214-0386</p>
    <p class="footer-line footer-web">hello@brightstarkids.com &nbsp; | &nbsp; www.brightstarkids.com</p>
    <p class="footer-line footer-address">48 Maple Field Rd, Springdale, Ohio 45000</p>
  </footer>
</div>
<div class="social" aria-label="Social links"><span></span><span></span><span></span></div>
</body>
</html>
```